Quillstone Ventures Wordpress Theme

My current wordpress is at: http://quillstoneventuers.blogspacehost.com/

I own the actual domain for mapping.

I'd like the look and feel to be like: http://brightlarchworks.com/

With the front page all black with my logo in the middle (see attached).

The colors should be consistent with my business cards (see attached)

I'd like it to be clean, simple and a little flashy.

Requirements
Must have
• space for intro video

Plug in ability in wordpress

Calendar of events

Clip Vault

```html
<!DOCTYPE html>
<html lang="en">
<head>
<meta charset="utf-8">
<title>Quillstone Ventures</title>
<link href="https://fonts.googleapis.com/css2?family=PT+Sans:wght@400;700&family=PT+Sans+Narrow:wght@400;700&display=swap" rel="stylesheet">
<style>
:root{
  --black:#000;
  --white:#fff;
  --red:#d21c1c;
  --red-band:#a10000;
  --red-deep:#4a0000;
  --red-link:#ff6a55;
  --grey-text:#c4c4c4;
  --grey-foot:#b5b5b5;
  --band:#262626;
  --social:#3d86c9;
}
*{margin:0;padding:0;box-sizing:border-box}
html,body{width:878px;height:1200px;overflow:hidden;background:var(--black)}
body{position:relative;font-family:"PT Sans",sans-serif;color:var(--white)}
.abs{position:absolute}

.main-nav{position:absolute;left:0;top:0;width:878px;height:47px;background:linear-gradient(#2c2c2c,#4a4a4a 60%,#5a5a5a)}
.main-nav a{position:absolute;top:17px;font-family:"PT Sans Narrow",sans-serif;font-size:13px;color:var(--white);text-decoration:none;text-transform:uppercase;white-space:nowrap}
.nav-divider{position:absolute;top:30px;width:1px;height:17px;background:#6d6d6d}

.hero{position:absolute;left:0;top:47px;width:878px;height:369px;background:linear-gradient(#1d1d1d,#2f2f2f 55%,#424242)}
.video-link{position:absolute;left:769px;top:82px;font-size:10px;font-weight:700;color:var(--red);text-transform:uppercase;letter-spacing:.2px}
.brand-mark{position:absolute;left:384px;top:140px;width:120px;height:120px;border-radius:50%;background:#8f8f8f}
.brand-name{position:absolute;left:0;width:878px;top:300px;text-align:center;font-size:24px;font-weight:700;color:#c9c9c9;letter-spacing:2px;text-transform:uppercase}

.service-band{position:absolute;left:0;top:416px;width:878px;height:124px;background:var(--band)}
.service-label{position:absolute;top:482px;font-family:"PT Sans Narrow",sans-serif;font-size:12.5px;color:var(--grey-text);text-transform:uppercase;white-space:nowrap;transform:translateX(-50%)}

.intro-title{left:21px;top:561px;font-size:13px;color:var(--red);text-transform:uppercase}
.intro-text{left:21px;top:588px;width:840px;font-size:14px;line-height:26px}

.feature{position:absolute;top:670px;width:232px}
.feature h3{font-size:10.5px;font-weight:400;line-height:15px;color:var(--red);text-transform:uppercase}
.feature p{font-size:11px;line-height:15.8px}

.events{position:absolute;left:10px;top:815px;width:858px;height:122px;background:var(--red-band)}
.events-title{left:60px;top:832px;font-size:11px;font-weight:700;color:var(--black);text-transform:uppercase}
.event{position:absolute;top:856px;width:260px;font-size:10.5px;line-height:16px}
.event h4{font-size:10.5px;color:var(--black)}
.event p{color:var(--red-deep)}
.event a{display:block;margin-top:7px;color:var(--red-link);text-decoration:none}

.footer-col{position:absolute;top:963px;font-size:10.5px;line-height:15.5px;color:var(--grey-foot)}
.footer-col h5{font-size:10.5px;color:var(--red)}
.footer-brand{left:774px;top:1000px;width:80px;text-align:center;font-size:9px;font-weight:700;color:#cfcfcf;text-transform:uppercase;line-height:11px}
.footer-label{top:1081px;font-size:10.5px;font-weight:700;color:var(--red)}
.footer-text{top:1100px;font-size:10.5px;color:var(--grey-foot)}
.social{position:absolute;top:1076px;width:28px;height:28px;border-radius:50%;background:var(--social)}
</style>
</head>
<body>

<nav class="main-nav">
  <a style="left:34px">Company</a>
  <span class="nav-divider" style="left:102px"></span>
  <a style="left:121px">Image &amp; Innovation</a>
  <span class="nav-divider" style="left:243px"></span>
  <a style="left:262px">Energy &amp; Technology</a>
  <span class="nav-divider" style="left:397px"></span>
  <a style="left:414px">Leadership &amp; Development</a>
  <span class="nav-divider" style="left:572px"></span>
  <a style="left:590px">Training &amp; Communication</a>
  <span class="nav-divider" style="left:754px"></span>
  <a style="left:770px">Luxury &amp; Living</a>
</nav>

<header class="hero"></header>
<svg class="abs" style="left:725px;top:60px" width="32" height="32" viewBox="0 0 32 32" aria-hidden="true">
  <circle cx="16" cy="16" r="15" fill="#fff"/>
  <circle cx="16" cy="8" r="3.6" fill="#222"/><circle cx="16" cy="24" r="3.6" fill="#222"/>
  <circle cx="8" cy="16" r="3.6" fill="#222"/><circle cx="24" cy="16" r="3.6" fill="#222"/>
  <circle cx="16" cy="16" r="1.6" fill="#222"/>
  <path d="M24 29 L31 31" stroke="#fff" stroke-width="3"/>
</svg>
<span class="video-link">Watch the video</span>
<div class="brand-mark" aria-hidden="true"></div>
<div class="brand-name">Quillstone Ventures</div>

<section class="service-band"></section>
<div class="abs" style="left:41px;top:441px;width:32px;height:32px;border-radius:50%;background:#bdbdbd" aria-hidden="true"></div>
<svg class="abs" style="left:158px;top:436px" width="28" height="40" viewBox="0 0 28 40" aria-hidden="true">
  <path d="M14 2a11 11 0 0 0-7 19.5c1.5 1.4 2 3 2 5h10c0-2 .5-3.6 2-5A11 11 0 0 0 14 2z" fill="none" stroke="#111" stroke-width="1.6"/>
  <path d="M9 29h10M9 32h10M11 35h6" stroke="#111" stroke-width="1.6"/>
</svg>
<svg class="abs" style="left:293px;top:435px" width="48" height="44" viewBox="0 0 48 44" aria-hidden="true">
  <g fill="none" stroke="#111" stroke-width="1.6">
    <ellipse cx="24" cy="22" rx="22" ry="8"/>
    <ellipse cx="24" cy="22" rx="22" ry="8" transform="rotate(60 24 22)"/>
    <ellipse cx="24" cy="22" rx="22" ry="8" transform="rotate(-60 24 22)"/>
  </g>
  <circle cx="24" cy="22" r="4" fill="#111"/>
</svg>
<svg class="abs" style="left:465px;top:441px" width="40" height="34" viewBox="0 0 40 34" aria-hidden="true">
  <path d="M2 4h11a5 5 0 1 1 8 0h10v10a5 5 0 1 1 0 8v10H2z" fill="#111"/>
</svg>
<svg class="abs" style="left:641px;top:443px" width="40" height="32" viewBox="0 0 40 32" aria-hidden="true">
  <path d="M2 11h7l10-9v28L9 21H2z" fill="none" stroke="#111" stroke-width="1.6"/>
  <path d="M24 10a8 8 0 0 1 0 12M28 6a14 14 0 0 1 0 20M32 2a20 20 0 0 1 0 28" fill="none" stroke="#111" stroke-width="1.6"/>
</svg>
<svg class="abs" style="left:780px;top:446px" width="54" height="28" viewBox="0 0 54 28" aria-hidden="true">
  <path d="M2 6l10 8 6-12 9 12 9-12 6 12 10-8-6 20H8z" fill="#111"/>
</svg>
<span class="service-label" style="left:57px">About us</span>
<span class="service-label" style="left:171px">Image &amp; Innovation</span>
<span class="service-label" style="left:317px">Energy &amp; Technology</span>
<span class="service-label" style="left:482px">Leadership &amp; Development</span>
<span class="service-label" style="left:660px">Training &amp; Communication</span>
<span class="service-label" style="left:809px">Luxury &amp; Living</span>

<h1 class="abs intro-title" style="font-weight:400">Lorem ipsum dolor sit amet, consectetur adipiscing elit.</h1>
<p class="abs intro-text">Donec massa elit, eleifend ut fermentum molestie, condimentum in mi. Etiam sollicitudin dui sed lectus dictum et suscipit turpis interdum. Sed dictum sapien non quam mattis fermentum. Morbi augue ipsum, facilisis in interdum vel, molestie quis metus.</p>

<article class="feature" style="left:21px"><h3>Lorem ipsum dolor sit amet, consectetur adipiscing elit.</h3><p>Donec massa elit, eleifend ut fermentum molestie, condimentum in mi. Etiam sollicitudin dui sed lectus dictum et suscipit turpis interdum. Sed dictum sapien non quam mattis fermentum. Morbi augue ipsum, facilisis in interdum vel, molestie quis metus.</p></article>
<article class="feature" style="left:318px"><h3>Lorem ipsum dolor sit amet, consectetur adipiscing elit.</h3><p>Donec massa elit, eleifend ut fermentum molestie, condimentum in mi. Etiam sollicitudin dui sed lectus dictum et suscipit turpis interdum. Sed dictum sapien non quam mattis fermentum. Morbi augue ipsum, facilisis in interdum vel, molestie quis metus.</p></article>
<article class="feature" style="left:613px"><h3>Lorem ipsum dolor sit amet, consectetur adipiscing elit.</h3><p>Donec massa elit, eleifend ut fermentum molestie, condimentum in mi. Etiam sollicitudin dui sed lectus dictum et suscipit turpis interdum. Sed dictum sapien non quam mattis fermentum. Morbi augue ipsum, facilisis in interdum vel, molestie quis metus.</p></article>

<section class="events"></section>
<svg class="abs" style="left:23px;top:823px" width="32" height="28" viewBox="0 0 32 28" aria-hidden="true">
  <rect x="1.5" y="4" width="29" height="22.5" rx="2" fill="none" stroke="#fff" stroke-width="2.4"/>
  <rect x="1.5" y="4" width="29" height="5" fill="#fff"/>
  <rect x="8" y="0.5" width="3" height="6" fill="#fff"/><rect x="21" y="0.5" width="3" height="6" fill="#fff"/>
  <text x="16" y="24" text-anchor="middle" font-family="PT Sans, sans-serif" font-weight="700" font-size="14" fill="#fff">5</text>
</svg>
<h2 class="abs events-title">Our calendar events</h2>
<div class="event" style="left:26px"><h4>Lorem ipsum dolor sit amet, consectetur adipiscing elit.</h4><p>Donec massa elit, eleifend ut fermentum molestie,<br>condimentum in mi.</p><a>view details of the event</a></div>
<div class="event" style="left:300px"><h4>Lorem ipsum dolor sit amet, consectetur adipiscing elit.</h4><p>Donec massa elit, eleifend ut fermentum molestie,<br>condimentum in mi.</p><a>view details of the event</a></div>
<div class="event" style="left:584px"><h4>Lorem ipsum dolor sit amet, consectetur adipiscing elit.</h4><p>Donec massa elit, eleifend ut fermentum molestie,<br>condimentum in mi.</p><a>view details of the event</a></div>

<footer>
  <div class="footer-col" style="left:26px"><h5>Company</h5>Image &amp; Innovation<br>Energy &amp; Technology<br>Leadership &amp; Development<br>Training &amp; Communication<br>Luxury &amp; Living</div>
  <div class="footer-col" style="left:180px"><h5>Company</h5>Image &amp; Innovation<br>Energy &amp; Technology<br>Leadership &amp; Development<br>Training &amp; Communication<br>Luxury &amp; Living</div>
  <div class="footer-col" style="left:325px"><h5>Company</h5>Image &amp; Innovation<br>Energy &amp; Technology<br>Leadership &amp; Development<br>Training &amp; Communication<br>Luxury &amp; Living</div>
  <div class="footer-col" style="left:480px"><h5>Company</h5>Image &amp; Innovation<br>Energy &amp; Technology<br>Leadership &amp; Development<br>Training &amp; Communication<br>Luxury &amp; Living</div>
  <div class="footer-col" style="left:642px"><h5>Company</h5>Image &amp; Innovation<br>Energy &amp; Technology<br>Leadership &amp; Development<br>Training &amp; Communication<br>Luxury &amp; Living</div>
  <div class="abs footer-brand">Quillstone Ventures</div>

  <span class="abs footer-label" style="left:27px">Our Address</span>
  <span class="abs footer-text" style="left:23px">Phasellus turpis urna, pulvinar ut vehicula eget,</span>
  <span class="abs footer-label" style="left:255px">Contact info</span>
  <span class="abs footer-text" style="left:255px">Phasellus turpis urna, pulvinar ut vehicula eget,</span>
  <span class="abs footer-label" style="left:478px;top:1085px">follow the lion!</span>
  <span class="social" style="left:554px" aria-hidden="true"></span>
  <span class="social" style="left:590px" aria-hidden="true"></span>
  <span class="social" style="left:626px" aria-hidden="true"></span>
  <span class="social" style="left:662px" aria-hidden="true"></span>
  <span class="social" style="left:698px" aria-hidden="true"></span>
  <span class="social" style="left:734px" aria-hidden="true"></span>
</footer>

</body>
</html>
```